Brightwell Recruit Homepage Redesign

Redevelopment work is underway on the Brightwell Recruit website www.brightwell-recruit.com - one task is to create a more compelling vertically stacked, mobile friendly homepage. The developers are not graphic designers and have been unable to produce an effective enough design. Their latest iteration can be seen @ http://dovemark.co.uk/brightwell_recruit/index_5.html

The goal of the current design job is to:

a) produce a homepage design - reworking the attached draft concepts/designs to produce an effective landing page that will entice visitors to respond to the key call to action - to book a meeting with me to discuss their needs
b) ensure the design is aesthetically/functionally aligned with the rest of the site
c) ensure the design supports responsive implementation for viewing on a full range of desktop browsers and mobile devices.

Final output should be in a .psd file with all layers unmerged.

Further details on uploaded docs.

```html
<!DOCTYPE html>
<html lang="en">
<head>
<meta charset="utf-8">
<title>Brightwell Recruit – Virtual Leadership Coaching</title>
<link href="https://fonts.googleapis.com/css2?family=Open+Sans:wght@300;400;600;700&family=Raleway:wght@400;500;600;700&display=swap" rel="stylesheet">
<style>
:root{
  --orange:#f28c1e;
  --orange-deep:#e57b10;
  --amber:#fbae17;
  --navy:#0e4477;
  --navy-dark:#0a2f55;
  --ink:#2b2b2b;
  --ink-soft:#3a3f47;
  --header-bg:#eef1f4;
  --rule:#c9ced4;
  --footer-text:#e8eef6;
  --sky-light:#c8f1fb;
  --sky-mid:#5cc3e6;
  --sky-deep:#2a8ac4;
  --white:#ffffff;
}
*{box-sizing:border-box;margin:0;padding:0}
html,body{width:1187px;height:1200px;overflow:hidden}
body{position:relative;background:var(--header-bg);font-family:"Open Sans",Arial,sans-serif;color:var(--ink)}
.abs{position:absolute}

/* header */
.top-rule{left:0;top:0;width:1187px;height:8px;background:var(--orange)}
.site-header{left:0;top:8px;width:1187px;height:188px;background:var(--header-bg)}
.header-rule{left:0;top:196px;width:1187px;height:7px;background:var(--orange)}
.brand{left:142px;top:38px;width:230px}
.brand-row{display:flex;align-items:center;gap:10px}
.brand-mark{width:34px;height:34px;border-radius:50%;background:var(--orange);flex:none}
.brand-name{font-family:"Open Sans",sans-serif;font-weight:700;font-size:24px;line-height:1.05;color:var(--navy)}
.brand-tagline{margin-top:18px;font-size:13px;color:var(--ink-soft);letter-spacing:-.2px}

.nav-col{top:8px;height:188px;border-left:1px solid var(--rule)}
.nav-main{left:382px;width:159px;padding:23px 0 0 6px}
.nav-services{left:541px;width:175px;padding:23px 0 0 6px;border-left:1px solid var(--navy)}
.nav-list{list-style:none}
.nav-list li{font-size:11.5px;font-weight:700;line-height:23.3px;color:#222;white-space:nowrap}
.nav-services .nav-list li{font-size:11px;font-weight:600}
.nav-list li.is-active{color:var(--orange);position:relative}
.nav-list li.is-active::after{content:"";position:absolute;left:147px;top:11px;width:17px;height:4px;background:var(--navy)}
.nav-tile{top:8px;height:188px;text-align:center}
.nav-tile svg{display:block;margin:20px auto 0}
.nav-tile span{display:block;margin-top:7px;font-size:17px;font-weight:600;line-height:23px;color:#1f2a36}
.tile-cert{left:716px;width:113px}
.tile-trans{left:829px;width:112px}
.tile-lang{left:941px;width:105px}
.tile-end{left:1046px;width:0}

/* hero */
.hero{left:0;top:203px;width:1187px;height:652px;overflow:hidden;
  background:radial-gradient(ellipse 620px 420px at 420px 330px,var(--sky-light) 0%,#8fdcf3 35%,var(--sky-mid) 70%,var(--sky-deep) 100%)}
.hero-photo{left:640px;top:0;width:547px;height:652px;
  background:linear-gradient(90deg,rgba(120,170,220,0) 0%,rgba(150,180,215,.55) 25%,rgba(170,185,205,.7) 60%,rgba(140,160,190,.6) 100%)}
.hero-headline{left:130px;top:100px;width:560px;text-align:center;font-weight:300;font-size:43px;line-height:55px;color:#2a2f36}
.hero-headline em{font-style:normal;font-weight:600;color:var(--orange)}
.cta-book{left:284px;top:312px;width:289px;height:74px;border-radius:3px;border:1px solid #062a4e;
  background:linear-gradient(#1a5a96,var(--navy-dark));display:flex;align-items:center;padding-left:18px;color:var(--white);text-decoration:none}
.cta-book svg{flex:none}
.cta-book span{margin-left:24px;font-size:21px;line-height:25px;font-weight:400;letter-spacing:.3px}
.hero-sub{left:120px;top:415px;width:540px;text-align:center;font-size:33px;line-height:45px;font-weight:300;color:#23282e}
.hero-sub .accent{color:var(--orange);font-weight:400}

.slide-arrow{top:280px;width:59px;height:59px;background:#1d2a33;display:flex;align-items:center;justify-content:center}
.slide-prev{left:0}
.slide-next{left:1128px}

/* feature panel */
.feature-panel{left:672px;top:48px;width:375px;height:571px;background:rgba(236,242,248,.85);border:1px solid #b8c2cc}
.panel-photo{left:14px;top:28px;width:160px;height:160px;border-radius:50%;border:4px solid #f2f4f6;
  background:radial-gradient(circle at 50% 45%,#4c5258 0%,#2b2f33 55%,#1a1c1e 100%);overflow:hidden}
.panel-photo b{position:absolute;left:46px;top:58px;font-family:"Raleway",sans-serif;font-weight:500;font-size:14px;line-height:20px;color:var(--amber)}
.panel-arrow{left:52px;top:196px}
.panel-updown{left:334px;top:17px;width:29px}
.panel-updown div{height:29px;display:flex;align-items:center;justify-content:center}
.panel-updown .up{background:#2c5f96}
.panel-updown .down{background:#2d3a46}
.panel-title{left:183px;top:67px;font-family:"Raleway",sans-serif;font-size:23px;line-height:27px;color:#333}
.panel-title .strong-navy{color:#1d4f86;font-weight:700}
.panel-title .strong-amber{color:var(--amber);font-weight:700}
.panel-list{left:128px;top:198px;list-style:none;font-family:"Raleway",sans-serif;font-size:15px;font-weight:500;color:#222}
.panel-list li{line-height:21.4px;display:flex;align-items:center;gap:8px;white-space:nowrap}
.panel-list svg{flex:none}
.read-more{left:127px;top:446px;width:97px;height:26px;border-radius:3px;border:1px solid #c47a10;background:linear-gradient(#fbb43a,#f19a1b);
  font-family:"Raleway",sans-serif;font-size:10.5px;font-weight:500;color:#2a2a2a;display:flex;align-items:center;justify-content:center}
.panel-dots{left:282px;top:548px;display:flex;gap:4px}
.panel-dots i{width:14px;height:14px;border-radius:3px;background:#858a90;display:block}
.panel-dots i.on{background:var(--amber)}

.hero-tab{left:572px;top:619px}

/* footer */
.footer-rule{left:0;top:855px;width:1187px;height:8px;background:var(--orange)}
.site-footer{left:0;top:863px;width:1187px;height:268px;background:var(--navy)}
.footer-col{top:41px;width:211px;color:var(--footer-text)}
.footer-heading{height:35px;border:2px solid #dfe7f0;display:flex;align-items:center;justify-content:center;font-size:14.5px;letter-spacing:.2px;color:var(--white)}
.footer-list{list-style:none;margin-top:19px;padding-left:10px;font-size:11.5px;line-height:19px}
.footer-list li::before{content:"•";color:#6f93bb;font-size:9px;margin-right:8px;position:relative;top:-1px}
.footer-contact{list-style:none;margin-top:16px;padding-left:29px;font-size:11.5px;line-height:19px}
.col-company{left:148px}
.col-services{left:375px}
.col-contact{left:603px}
.col-news{left:829px}
.news-input{margin-top:30px;width:209px;height:33px;background:#eef1f4;border:1px solid #d4dae0;font-size:11.5px;color:#555;padding:9px 15px}
.news-send{margin:14px 0 0 161px;width:48px;height:33px;border:2px solid var(--amber);color:var(--amber);font-size:13px;display:flex;align-items:center;justify-content:center}

/* bottom bar */
.bottom-bar{left:0;top:1131px;width:1187px;height:69px;background:var(--header-bg)}
.social-bar{left:139px;top:19px;width:232px;height:33px;background:#c9ccd0;display:flex;align-items:center;padding-left:25px;gap:5px}
.social-bar .lead{width:32px;height:33px;background:#1d2a4a;margin-right:4px}
.social-bar i{width:23px;height:23px;background:#1d2a4a;display:block}
.copyright{right:146px;top:27px;font-size:12px;color:#333}
</style>
</head>
<body>

<div class="abs top-rule"></div>
<header class="abs site-header" aria-label="Site header"></header>

<div class="abs brand">
  <div class="brand-row">
    <span class="brand-mark"></span>
    <span class="brand-name">Brightwell Recruit</span>
  </div>
  <p class="brand-tagline">Online Leadership Coaching &amp; Assessment</p>
</div>

<nav class="abs nav-col nav-main">
  <ul class="nav-list">
    <li>Home</li>
    <li class="is-active">Transforming Leader</li>
    <li>Assesments</li>
    <li>Coaching</li>
    <li>Resources &amp; Tool</li>
    <li>Bookings &amp; Prices</li>
  </ul>
</nav>
<nav class="abs nav-col nav-services">
  <ul class="nav-list">
    <li>Business Translation Services</li>
    <li>Legal Translation Services</li>
    <li>Official Translation Services</li>
    <li>Medical Translation Services</li>
    <li>Technical Translate Services</li>
    <li>Financial Translation Services</li>
  </ul>
</nav>

<div class="abs nav-col nav-tile tile-cert">
  <svg width="60" height="60" viewBox="0 0 60 60" aria-hidden="true">
    <g fill="#f7b21b">
      <circle cx="30" cy="30" r="22"/>
      <g transform="translate(30 30)">
        <rect x="-3" y="-29" width="6" height="9"/><rect x="-3" y="20" width="6" height="9"/>
        <rect x="-29" y="-3" width="9" height="6"/><rect x="20" y="-3" width="9" height="6"/>
        <rect x="-3" y="-29" width="6" height="9" transform="rotate(45)"/><rect x="-3" y="-29" width="6" height="9" transform="rotate(135)"/>
        <rect x="-3" y="-29" width="6" height="9" transform="rotate(225)"/><rect x="-3" y="-29" width="6" height="9" transform="rotate(315)"/>
      </g>
    </g>
    <circle cx="30" cy="30" r="15" fill="none" stroke="#fff" stroke-width="3"/>
    <path d="M23 30l5 5 10-11" fill="none" stroke="#fff" stroke-width="3.5" stroke-linecap="round" stroke-linejoin="round"/>
  </svg>
  <span>Certified<br>Brightwell</span>
</div>
<div class="abs nav-col nav-tile tile-trans">
  <svg width="60" height="60" viewBox="0 0 60 60" aria-hidden="true">
    <rect x="5" y="6" width="30" height="30" rx="3" fill="#f7b21b"/>
    <rect x="24" y="24" width="30" height="30" rx="3" fill="#f7b21b" stroke="#eef1f4" stroke-width="2"/>
    <path d="M12 15h16M20 12v3M14 27c5-3 9-8 10-12M16 19c2 4 6 7 10 8" fill="none" stroke="#fff" stroke-width="2.4" stroke-linecap="round"/>
    <path d="M32 48l7-17 7 17M35 42h8" fill="none" stroke="#fff" stroke-width="3" stroke-linejoin="round"/>
  </svg>
  <span>Translation<br>Services</span>
</div>
<div class="abs nav-col nav-tile tile-lang">
  <svg width="60" height="60" viewBox="0 0 60 60" aria-hidden="true">
    <path d="M4 14h22v18H14l-6 6v-6H4z" fill="#f9c24c"/>
    <path d="M16 6h40v28H34l-9 9v-9h-9z" fill="#f7b21b" stroke="#eef1f4" stroke-width="2"/>
    <circle cx="28" cy="20" r="2.6" fill="#fff"/><circle cx="36" cy="20" r="2.6" fill="#fff"/><circle cx="44" cy="20" r="2.6" fill="#fff"/>
  </svg>
  <span>Languages<br>Offered</span>
</div>
<div class="abs nav-col tile-end"></div>

<div class="abs header-rule"></div>

<section class="abs hero" aria-label="Leadership coaching introduction">
  <div class="abs hero-photo" role="img" aria-label="Photo of a leader in a blue shirt and patterned tie, gesturing with both hands"></div>

  <h1 class="abs hero-headline">Want to <em>motivate</em> your<br>team to higher<br>performance levels?</h1>

  <a class="abs cta-book" href="#book">
    <svg width="46" height="42" viewBox="0 0 46 42" aria-hidden="true" fill="#fff">
      <circle cx="23" cy="5" r="4.5"/>
      <rect x="17" y="11" width="12" height="12" rx="2"/>
      <circle cx="8" cy="11" r="3.5"/><circle cx="38" cy="11" r="3.5"/>
      <rect x="3" y="16" width="4" height="20"/><rect x="39" y="16" width="4" height="20"/>
      <rect x="11" y="24" width="24" height="4"/><rect x="21" y="28" width="4" height="12"/>
      <rect x="7" y="26" width="4" height="10"/><rect x="35" y="26" width="4" height="10"/>
    </svg>
    <span>BOOK A<br>MEETING NOW</span>
  </a>

  <p class="abs hero-sub">Brightwell Recruit<br><span class="accent">Virtual Leadership Coaching</span><br>&amp; Assessment</p>

  <div class="abs slide-arrow slide-prev"><svg width="18" height="28" viewBox="0 0 18 28" aria-hidden="true"><path d="M15 2L3 14l12 12" fill="none" stroke="#fff" stroke-width="2"/></svg></div>
  <div class="abs slide-arrow slide-next"><svg width="18" height="28" viewBox="0 0 18 28" aria-hidden="true"><path d="M3 2l12 12L3 26" fill="none" stroke="#fff" stroke-width="2"/></svg></div>

  <aside class="abs feature-panel">
    <svg class="abs panel-arrow" width="80" height="368" viewBox="0 0 80 368" aria-hidden="true">
    <path d="M21 0h38v292h21L40 368 0 292h21z" fill="var(--amber)"/>
    </svg>
    <div class="abs panel-photo" role="img" aria-label="Close-up photo of a car dashboard gauge">
      <b>NEED A<br>BOOST?</b>
    </div>
    <div class="abs panel-updown">
      <div class="up"><svg width="14" height="8" viewBox="0 0 14 8" aria-hidden="true"><path d="M1 7l6-6 6 6" fill="none" stroke="#fff" stroke-width="1.5"/></svg></div>
      <div class="down"><svg width="14" height="8" viewBox="0 0 14 8" aria-hidden="true"><path d="M1 1l6 6 6-6" fill="none" stroke="#fff" stroke-width="1.5"/></svg></div>
    </div>
    <h2 class="abs panel-title" style="font-weight:400">YOU ARE<br>THE LEADER<br><span class="strong-navy">YOUR PEOPLE</span><br><span class="strong-amber">EXPECT YOU TO:</span></h2>
    <ul class="abs panel-list">
      <li><svg width="18" height="10" viewBox="0 0 18 10" aria-hidden="true"><path d="M0 5h13M10 1l6 4-6 4" fill="none" stroke="#163e6e" stroke-width="2.4"/></svg>Engage them</li>
      <li><svg width="18" height="10" viewBox="0 0 18 10" aria-hidden="true"><path d="M0 5h13M10 1l6 4-6 4" fill="none" stroke="#163e6e" stroke-width="2.4"/></svg>Inspire them</li>
      <li><svg width="18" height="10" viewBox="0 0 18 10" aria-hidden="true"><path d="M0 5h13M10 1l6 4-6 4" fill="none" stroke="#163e6e" stroke-width="2.4"/></svg>Motivate them</li>
      <li><svg width="18" height="10" viewBox="0 0 18 10" aria-hidden="true"><path d="M0 5h13M10 1l6 4-6 4" fill="none" stroke="#163e6e" stroke-width="2.4"/></svg>Develop them</li>
      <li><svg width="18" height="10" viewBox="0 0 18 10" aria-hidden="true"><path d="M0 5h13M10 1l6 4-6 4" fill="none" stroke="#163e6e" stroke-width="2.4"/></svg>Set vision</li>
      <li><svg width="18" height="10" viewBox="0 0 18 10" aria-hidden="true"><path d="M0 5h13M10 1l6 4-6 4" fill="none" stroke="#163e6e" stroke-width="2.4"/></svg>Define values</li>
      <li><svg width="18" height="10" viewBox="0 0 18 10" aria-hidden="true"><path d="M0 5h13M10 1l6 4-6 4" fill="none" stroke="#163e6e" stroke-width="2.4"/></svg>Create culture</li>
      <li><svg width="18" height="10" viewBox="0 0 18 10" aria-hidden="true"><path d="M0 5h13M10 1l6 4-6 4" fill="none" stroke="#163e6e" stroke-width="2.4"/></svg>Resolve conflicts</li>
      <li><svg width="18" height="10" viewBox="0 0 18 10" aria-hidden="true"><path d="M0 5h13M10 1l6 4-6 4" fill="none" stroke="#163e6e" stroke-width="2.4"/></svg>Solve problems</li>
      <li><svg width="18" height="10" viewBox="0 0 18 10" aria-hidden="true"><path d="M0 5h13M10 1l6 4-6 4" fill="none" stroke="#163e6e" stroke-width="2.4"/></svg>Choose winning strategies</li>
      <li><svg width="18" height="10" viewBox="0 0 18 10" aria-hidden="true"><path d="M0 5h13M10 1l6 4-6 4" fill="none" stroke="#163e6e" stroke-width="2.4"/></svg>Take care of business as usual.</li>
    </ul>
    <div class="abs read-more">READ MORE</div>
    <div class="abs panel-dots"><i class="on"></i><i></i><i></i><i></i><i></i></div>
  </aside>

  <svg class="abs hero-tab" width="40" height="33" viewBox="0 0 40 33" aria-hidden="true">
    <path d="M20 0L40 33H0z" fill="var(--amber)"/>
    <path d="M20 15v14M13 22h14" stroke="#1a1a1a" stroke-width="3"/>
  </svg>
</section>

<div class="abs footer-rule"></div>
<footer class="abs site-footer">
  <div class="abs footer-col col-company">
    <div class="footer-heading">COMPANY</div>
    <ul class="footer-list">
      <li>About us</li><li>Career</li><li>Our works / References</li><li>Contact us</li>
    </ul>
  </div>
  <div class="abs footer-col col-services">
    <div class="footer-heading">OUR SERVICES</div>
    <ul class="footer-list">
      <li>Lorem ipsum</li><li>Dolor sit amet</li><li>Nullam in ultricies</li><li>Vestibulum at sapie</li>
    </ul>
  </div>
  <div class="abs footer-col col-contact">
    <div class="footer-heading">CONTACT US</div>
    <ul class="footer-contact">
      <li>Live Chat By Email</li><li>By Phone: 1.800.555.0142</li><li>Translation Service Quotes</li>
      <li>Translation Services</li><li>General Information</li><li>All Departments &amp; Divisions</li>
    </ul>
  </div>
  <div class="abs footer-col col-news">
    <div class="footer-heading">NEWS LETTER</div>
    <div class="news-input">E-mail Address ...</div>
    <div class="news-send">SEND</div>
  </div>
</footer>

<div class="abs bottom-bar">
  <div class="abs social-bar" aria-label="Social links">
    <span class="lead"></span><i></i><i></i><i></i><i></i><i></i><i></i>
  </div>
  <p class="abs copyright">Copyright 2014 All Right Reserved.</p>
</div>

</body>
</html>
```